Engineering and Energy service provider

We need a design that gives the impression of a high level of technical competence and a reliable partner. Simple structure with little need for updates.
The company brand is Volnar and today consists of two main businesses: energy optimisation (Volnar energy) and technical consultancy (Volnar Engineering). Volnar energy is shown in the attached powerpoint,
We are a young growing company that consists of several businesses, the largest parts are energy monitoring services and consulting services. Consulting services for commercial installations in the technical area of cooling, ventilation, heating and energy. Services offered include project planning, project management, inspection, operational analysis and technical investigations. Energy monitoring and optimization services are performed as a subscription with a subscription to the service.
Target Market(s)
Commercial property owners Grocery retail, grocery stores, construction companies
Industry/Entity Type
energy services and consulting services
Coding
Coded - Design and coding required
Number of Pages Required
5+ page
Look and feel
Each slider illustrates characteristics of the customer's brand and the style your logo design should communicate.

```html
<!DOCTYPE html>
<html lang="en">
<head>
<meta charset="UTF-8">
<title>Volnar — Smart Energy. Reliable Results.</title>
<link rel="stylesheet" href="https://fonts.googleapis.com/css2?family=Syncopate:wght@400;700&family=Montserrat:wght@400;500;600;700&display=swap">
<style>
:root{
  --blue:#0a5bbd;
  --blue-deep:#0747a6;
  --blue-ink:#0c2f6b;
  --orange:#f26b1d;
  --amber:#f7a700;
  --yellow:#f6c500;
  --ink:#1d1d1f;
  --muted:#5c6270;
  --white:#ffffff;
  --pale:#dce7f4;
}
*{margin:0;padding:0;box-sizing:border-box}
html,body{width:1200px;height:4383px;overflow:hidden}
body{position:relative;background:var(--white);font-family:"Montserrat",Arial,sans-serif;color:var(--ink)}
.display{font-family:"Syncopate","Arial Black",sans-serif;font-weight:700;text-transform:uppercase;line-height:.95;letter-spacing:-.02em}
.abs{position:absolute}
.btn{display:inline-block;background:linear-gradient(90deg,var(--orange),var(--amber));color:var(--white);font-weight:700;font-size:13px;text-transform:uppercase;padding:15px 28px;letter-spacing:.02em}
.btn-white{background:var(--white);color:var(--ink)}
.photo{display:block}

/* header */
.site-header{position:absolute;left:0;top:0;width:1200px;height:88px;background:var(--white);z-index:3}
.brand{position:absolute;left:90px;top:25px;font-family:"Syncopate",sans-serif;font-weight:700;font-size:34px;color:var(--blue);letter-spacing:.04em}
.nav{position:absolute;left:410px;top:36px;display:flex;gap:28px;font-size:12.5px;color:#333;text-transform:uppercase}
.nav .active{color:var(--orange);font-weight:600}
.header-cta{position:absolute;left:969px;top:22px;padding:14px 28px;font-size:12px}

/* hero */
.hero{position:absolute;left:0;top:88px;width:1200px;height:800px}
.hero svg{position:absolute;left:0;top:0}
.hero-title{left:90px;top:218px;color:var(--white);font-size:70px}
.hero-sub{left:90px;top:372px;color:var(--white);font-size:30px}
.hero-text{left:90px;top:424px;width:400px;color:var(--white);font-size:15px;line-height:1.4}
.hero-btn{left:90px;top:492px}

/* about */
.about-frame{left:190px;top:1072px;width:332px;height:428px;border:3px solid var(--amber);border-left:none;border-top:none}
.about-frame-2{left:190px;top:1072px;width:332px;height:428px;border-bottom:3px solid var(--orange);border-right:3px solid transparent}
.about-photo-a{left:142px;top:1026px;width:360px;height:452px;background:linear-gradient(160deg,#7a8896,#c46a2e 55%,#3b3d42)}
.about-photo-b{left:297px;top:1280px;width:267px;height:254px;background:var(--white);padding:6px;box-shadow:0 12px 30px rgba(0,0,0,.18)}
.about-photo-b .photo{width:100%;height:100%;background:linear-gradient(150deg,#d9dfe6,#7d8c9c 60%,#2b3645)}
.about-title{left:643px;top:1132px;font-size:32px;color:var(--ink)}
.about-kicker{left:643px;top:1217px;font-family:"Syncopate",sans-serif;font-weight:700;font-size:10.5px;text-transform:uppercase}
.about-text{left:643px;top:1249px;width:420px;font-size:13px;line-height:1.65;color:var(--muted)}
.about-btn{left:643px;top:1381px}

/* services */
.services{position:absolute;left:0;top:1628px;width:1200px;height:805px}
.services svg{position:absolute;left:0;top:0}
.services-title{left:0;width:1200px;top:236px;text-align:center;color:var(--white);font-size:30px}
.services-sub{left:0;width:1200px;top:283px;text-align:center;color:var(--white);font-size:13.5px}
.service{position:absolute;width:220px;text-align:center;color:var(--white)}
.service svg{position:static;display:block;margin:0 auto}
.service h3{font-family:"Syncopate",sans-serif;font-weight:700;font-size:13px;text-transform:uppercase;line-height:1.3;margin-top:14px}
.service p{font-size:12.5px;line-height:1.4;margin-top:10px}

/* optimisation */
.opt-title{left:122px;top:2612px;font-size:36px;line-height:.95}
.opt-text{left:122px;top:2734px;width:460px;font-size:13px;line-height:1.7;color:var(--muted)}
.opt-btn{left:122px;top:2858px}

/* sectors */
.sector{position:absolute;top:3077px;width:188px;height:280px}
.sector .photo{width:100%;height:100%}
.sector span{position:absolute;left:22px;bottom:38px;color:var(--white);font-family:"Syncopate",sans-serif;font-weight:700;font-size:10.5px;text-transform:uppercase;line-height:1.3}
.sectors-title{left:778px;top:3132px;font-size:34px}
.sectors-text{left:778px;top:3273px;width:300px;font-size:13px;line-height:1.65;color:var(--muted)}

/* cta */
.cta{position:absolute;left:0;top:3460px;width:1200px;height:923px}
.cta svg{position:absolute;left:0;top:0}
.cta-title{left:0;width:1200px;top:165px;text-align:center;color:var(--white);font-size:36px}
.cta-sub{left:0;width:1200px;top:225px;text-align:center;color:var(--white);font-size:14px}
.cta-btn{left:500px;top:270px;padding:15px 44px;font-size:12.5px}

/* footer */
.footer-brand{left:90px;top:4070px;font-family:"Syncopate",sans-serif;font-weight:700;font-size:44px;color:var(--white);letter-spacing:.04em}
.social{left:122px;top:4133px;display:flex;gap:11px}
.fcol{position:absolute;top:4033px;color:var(--white)}
.fcol h4{font-family:"Syncopate",sans-serif;font-weight:700;font-size:12.5px;text-transform:uppercase;margin-bottom:22px}
.fcol ul{list-style:none}
.fcol li{font-size:12px;margin-bottom:15px}
.fcol p{font-size:12px;line-height:1.5;width:320px}
.subscribe{display:flex;margin-top:14px;width:327px;height:46px;background:var(--white);border:2px solid var(--white);border-radius:3px}
.subscribe span{flex:1;font-size:12px;color:#888;padding:14px 14px}
.subscribe b{background:var(--blue);color:var(--white);font-size:11px;padding:14px 18px;text-transform:uppercase}
.footer-rule{left:40px;top:4320px;width:1120px;height:1px;background:rgba(255,255,255,.2)}
.copyright{left:0;width:1200px;top:4352px;text-align:center;color:var(--white);font-family:"Syncopate",sans-serif;font-weight:700;font-size:11px;text-transform:uppercase}
.chat{left:1126px;top:4282px}
</style>
</head>
<body>

<header class="site-header">
  <div class="brand">VOLNAR</div>
  <nav class="nav">
    <span class="active">Home</span><span>About us</span><span>Services</span><span>Industries</span><span>Latest news</span><span>Careers</span>
  </nav>
  <span class="btn header-cta">Contact us</span>
</header>

<section class="hero">
  <svg width="1200" height="800" viewBox="0 0 1200 800" aria-hidden="true">
    <defs>
      <linearGradient id="heroBlue" x1="0" y1="0" x2="1" y2="1">
        <stop offset="0" stop-color="#0c63c6"/><stop offset="1" stop-color="#0747a6"/>
      </linearGradient>
      <linearGradient id="heroStripe" x1="0" y1="1" x2="0" y2="0">
        <stop offset="0" stop-color="#f26b1d"/><stop offset="1" stop-color="#f7c300"/>
      </linearGradient>
      <linearGradient id="heroPhoto" x1="0" y1="0" x2="1" y2="1">
        <stop offset="0" stop-color="#5b7ea6"/><stop offset=".5" stop-color="#24374f"/><stop offset="1" stop-color="#141c28"/>
      </linearGradient>
    </defs>
    <polygon points="0,0 1200,0 1200,678 690,797 0,680" fill="url(#heroBlue)"/>
    <polygon points="448,0 1200,0 1200,678 690,797 440,748 660,420" fill="url(#heroStripe)"/>
    <g role="img" aria-label="Photo of engineers in hard hats reviewing plans at a table">
      <polygon points="470,0 1200,0 1200,678 690,797 465,752 682,420" fill="url(#heroPhoto)"/>
    </g>
  </svg>
  <h1 class="abs display hero-title">Smart<br>Energy.</h1>
  <p class="abs display hero-sub">Reliable results.</p>
  <p class="abs hero-text">Empowering commercial buildings with intelligent monitoring, optimization, and consulting solutions.</p>
  <span class="abs btn hero-btn">Get a consultation</span>
</section>

<section class="about">
  <div class="abs about-frame"></div>
  <div class="abs about-frame-2"></div>
  <div class="abs photo about-photo-a" role="img" aria-label="Photo of a technician in a safety helmet inspecting a ventilation unit"></div>
  <div class="abs about-photo-b"><div class="photo" role="img" aria-label="Photo of an engineer reviewing monitoring data on a computer"></div></div>
  <h2 class="abs display about-title">Your partner<br>in energy</h2>
  <p class="abs about-kicker">Efficiency and technical excellence</p>
  <p class="abs about-text">We are a young and growing company with a strong technical background in energy monitoring and consulting. Our team specializes in cooling, ventilation, heating, and energy systems — delivering data-driven insights and reliable solutions for commercial installations.</p>
  <span class="abs btn about-btn">Explore our services</span>
</section>

<section class="services">
  <svg width="1200" height="805" viewBox="0 0 1200 805" aria-hidden="true">
    <defs>
      <linearGradient id="bandOrange" x1="0" y1="0" x2="1" y2="0">
        <stop offset="0" stop-color="#f26b1d"/><stop offset="1" stop-color="#f7c300"/>
      </linearGradient>
    </defs>
    <polygon points="0,0 690,130 1200,0 1200,680 690,803 0,680" fill="url(#bandOrange)"/>
    <polygon points="0,0 690,150 1200,0 1200,662 690,780 0,662" fill="#0a5bbd"/>
    <polygon points="0,0 690,130 1200,0 1200,20 690,150 0,20" fill="#dce7f4" opacity="0"/>
    <polygon points="0,0 690,130 1200,0" fill="#ffffff"/>
    <polygon points="0,0 690,130 1200,0 1200,8 690,150 0,18" fill="#cfdcee"/>
  </svg>
  <h2 class="abs display services-title">Our services</h2>
  <p class="abs services-sub">Comprehensive support for every stage of your technical and energy projects.</p>

  <div class="service" style="left:91px;top:355px">
    <svg width="115" height="100" viewBox="0 0 115 100" aria-hidden="true">
      <polygon points="28,0 87,0 115,50 87,100 28,100 0,50" fill="#f28a12"/>
      <circle cx="57" cy="52" r="18" fill="none" stroke="#fff" stroke-width="2.5"/>
      <path d="M57 52 L66 42 M49 28 L57 20 L65 28" fill="none" stroke="#fff" stroke-width="2.5"/>
    </svg>
    <h3>Energy<br>monitoring &amp;<br>optimization</h3>
    <p>Monitor, analyze, and improve<br>your energy performance...</p>
  </div>
  <div class="service" style="left:356px;top:338px">
    <svg width="115" height="100" viewBox="0 0 115 100" aria-hidden="true">
      <polygon points="28,0 87,0 115,50 87,100 28,100 0,50" fill="#f28a12"/>
      <rect x="40" y="28" width="28" height="40" fill="none" stroke="#fff" stroke-width="2.5"/>
      <path d="M45 38h18M45 46h18M45 54h10" stroke="#fff" stroke-width="2.5"/>
      <circle cx="72" cy="62" r="9" fill="#f28a12" stroke="#fff" stroke-width="2.5"/>
    </svg>
    <h3>Operational<br>analysis...</h3>
    <p>From design to completion, our<br>experts ensure every project...</p>
  </div>
  <div class="service" style="left:622px;top:355px">
    <svg width="115" height="100" viewBox="0 0 115 100" aria-hidden="true">
      <polygon points="28,0 87,0 115,50 87,100 28,100 0,50" fill="#f28a12"/>
      <rect x="52" y="28" width="24" height="26" fill="none" stroke="#fff" stroke-width="2.5"/>
      <circle cx="46" cy="52" r="6" fill="none" stroke="#fff" stroke-width="2.5"/>
      <path d="M34 74c0-9 6-14 12-14s12 5 12 14" fill="none" stroke="#fff" stroke-width="2.5"/>
    </svg>
    <h3>Project<br>planning &amp;<br>management</h3>
    <p>From design to completion, our<br>experts ensure every project...</p>
  </div>
  <div class="service" style="left:889px;top:338px">
    <svg width="115" height="100" viewBox="0 0 115 100" aria-hidden="true">
      <polygon points="28,0 87,0 115,50 87,100 28,100 0,50" fill="#f28a12"/>
      <circle cx="57" cy="34" r="10" fill="none" stroke="#fff" stroke-width="2.5"/>
      <circle cx="45" cy="62" r="6" fill="none" stroke="#fff" stroke-width="2.5"/>
      <circle cx="69" cy="62" r="6" fill="none" stroke="#fff" stroke-width="2.5"/>
    </svg>
    <h3>Technical<br>consulting</h3>
    <p>Detailed inspections and<br>performance analyses...</p>
  </div>
</section>

<section class="optimisation">
  <h2 class="abs display opt-title">Continuous<br>energy optimization<br>simplified</h2>
  <p class="abs opt-text">Our subscription-based energy monitoring platform provides real-time insights, regular reports, and optimization recommendations — helping you reduce costs and environmental impact without extra effort.</p>
  <span class="abs btn opt-btn">Subscribe now</span>
  <svg class="abs" style="left:660px;top:2560px" width="420" height="410" viewBox="0 0 420 410" aria-hidden="true">
    <defs>
      <linearGradient id="hexPhoto" x1="0" y1="0" x2="1" y2="1">
        <stop offset="0" stop-color="#6f9fcf"/><stop offset=".55" stop-color="#2c4763"/><stop offset="1" stop-color="#1a2433"/>
      </linearGradient>
    </defs>
    <polygon points="130,55 330,55 415,212 330,368 130,368 42,212" fill="#fde0a8"/>
    <g role="img" aria-label="Photo of a man working on a laptop in a technical plant">
      <polygon points="110,12 355,12 415,170 355,372 110,372 0,195" fill="url(#hexPhoto)" transform="translate(0,0)"/>
    </g>
  </svg>
</section>

<section class="sectors">
  <div class="sector" style="left:123px"><div class="photo" role="img" aria-label="Photo of a commercial property owner with a tablet" style="background:linear-gradient(170deg,#e2e5e8,#6b7480 55%,#2d3440)"></div><span>Commercial<br>property owners</span></div>
  <div class="sector" style="left:327px"><div class="photo" role="img" aria-label="Photo of a grocery retail manager in a store" style="background:linear-gradient(170deg,#d8d3cc,#8a7f74 55%,#3a3532)"></div><span>Grocery retail<br>&amp; supermarkets</span></div>
  <div class="sector" style="left:531px"><div class="photo" role="img" aria-label="Photo of construction professionals in hard hats" style="background:linear-gradient(170deg,#e8e2d0,#8c7c5a 50%,#343038)"></div><span>Construction<br>companies</span></div>
  <h2 class="abs display sectors-title">Trusted by<br>leading<br>commercial<br>sectors</h2>
  <p class="abs sectors-text">We deliver energy-efficient and technically sound solutions across industries:</p>
</section>

<section class="cta">
  <svg width="1200" height="923" viewBox="0 0 1200 923" aria-hidden="true">
    <defs>
      <linearGradient id="ctaGrad" x1="0" y1="1" x2="1" y2="0">
        <stop offset="0" stop-color="#f26b1d"/><stop offset=".55" stop-color="#f49a10"/><stop offset="1" stop-color="#f3c700"/>
      </linearGradient>
    </defs>
    <polygon points="0,110 690,0 1200,110 1200,923 0,923" fill="url(#ctaGrad)"/>
    <polygon points="0,495 690,385 1200,440 1200,923 0,923" fill="#f7c300" opacity=".35"/>
    <polygon points="0,506 690,387 1200,506 1200,923 0,923" fill="#0a5bbd"/>
  </svg>
  <h2 class="abs display cta-title">Kestral energy solutions</h2>
  <p class="abs cta-sub">Reliable partner for energy monitoring and technical consulting.</p>
  <span class="abs btn btn-white cta-btn">Subscribe now</span>
</section>

<footer>
  <div class="abs footer-brand">VOLNAR</div>
  <div class="abs social">
    <svg width="176" height="48" viewBox="0 0 176 48" aria-label="Social links">
      <g fill="#2a74cf">
        <polygon points="14,2 40,2 54,24 40,46 14,46 0,24"/>
        <polygon points="75,2 101,2 115,24 101,46 75,46 61,24"/>
        <polygon points="136,2 162,2 176,24 162,46 136,46 122,24"/>
      </g>
      <g fill="none" stroke="#fff" stroke-width="2">
        <rect x="20" y="17" width="14" height="14" rx="2"/>
        <rect x="81" y="17" width="14" height="14" rx="2"/>
        <rect x="142" y="17" width="14" height="14" rx="2"/>
      </g>
    </svg>
  </div>
  <div class="fcol" style="left:405px">
    <h4>Quick link</h4>
    <ul><li>About Us</li><li>Our Services</li><li>Projects</li><li>Blog</li><li>Contact Us</li></ul>
  </div>
  <div class="fcol" style="left:582px">
    <h4>Subscribe newsletter</h4>
    <p>Get our monthly newsletter and marketing tips, straight to your inbox</p>
    <div class="subscribe"><span>Enter your email</span><b>Subscribe</b></div>
  </div>
  <div class="fcol" style="left:968px">
    <h4>Information</h4>
    <ul><li>Have feedback?</li><li>Let us know!</li><li>Privacy Policy</li><li>Terms of Use</li><li>Locations</li></ul>
  </div>
  <div class="abs footer-rule"></div>
  <p class="abs copyright">© 2025 Global Volnar. All rights reserved.</p>
  <svg class="abs chat" width="60" height="52" viewBox="0 0 60 52" aria-label="Chat">
    <polygon points="15,0 45,0 60,26 45,52 15,52 0,26" fill="#f28a12"/>
    <path d="M18 17h24v15H28l-6 5v-5h-4z" fill="#fff"/>
  </svg>
</footer>

</body>
</html>
```